Business Card design for a mini spa

business card for a small natural skincare/waxing spa. I need a modern, clean, classy card that draws people in but also need to be able to write future appointments on one side of it.

Target Market(s)

women age 16-70

Industry/Entity Type

Beauty Salon

Contact Information for Business Card

Petal Mist Care 907-318-2957
2865 W Tamsen Sitkin Harbor, AK 99672
Facial, Waxing, Spray Tanning,

Colors
33b8a4

Requirements
Must have
• Petal logo with flower
• my tag line "calm roots bright petals"
• 907-318-2957
• 2865 W Tamsen
• a place to write ......Your Next Appointment
• Mira Trelawney
Nice to have
• something modern, elegant, clean and simple with my attached logo. I also attached a few pictures of what I like along with a color pallet and a few fonts that I like.
Should not have
• no pictures of people in a spa I do not want your typical spa pictures like stone, people receiving a treatment.

```html
<!DOCTYPE html>
<html lang="en">
<head>
<meta charset="utf-8">
<title>Petal Mist Care – Business Card</title>
<link rel="stylesheet" href="https://fonts.googleapis.com/css2?family=Josefin+Sans:wght@300;400&family=Dancing+Script:wght@500&display=swap">
<style>
  :root {
    --stage: #2c2c2c;
    --aqua-card: #d6efec;
    --aqua-card-light: #e6f5f3;
    --white-card: #ffffff;
    --teal: #33b8a4;
    --teal-soft: #5cc6c6;
    --gold: #c8a97a;
    --gold-dot: #d8bf97;
  }
  * { margin: 0; padding: 0; box-sizing: border-box; }
  html, body {
    width: 1200px; height: 660px; overflow: hidden;
    background: var(--stage);
  }
  .stage {
    position: relative; width: 1200px; height: 660px;
    display: flex; align-items: center; justify-content: center; gap: 50px;
  }
  .card {
    position: relative; width: 525px; height: 300px;
    box-shadow: 0 10px 26px rgba(0,0,0,.45);
    font-family: "Josefin Sans", sans-serif;
  }

  /* Front */
  .card--front {
    background: linear-gradient(160deg, var(--aqua-card-light), var(--aqua-card));
    display: flex; flex-direction: column; align-items: center; justify-content: center;
  }
  .brand-front {
    display: flex; align-items: center; gap: 14px;
    color: var(--gold); font-weight: 300; font-size: 46px; letter-spacing: 1px;
  }
  .brand-dot { width: 18px; height: 18px; border-radius: 50%; background: var(--teal-soft); }
  .front-rule {
    width: 300px; height: 2px; background: var(--teal-soft); margin: 22px 0 14px;
  }
  .tagline {
    font-family: "Dancing Script", cursive;
    font-size: 30px; color: var(--gold); letter-spacing: .5px;
  }

  /* Back */
  .card--back { background: var(--white-card); }
  .brand-back {
    position: absolute; left: 30px; top: 92px;
    display: flex; align-items: center; gap: 9px;
    color: var(--teal-soft); font-weight: 300; font-size: 26px;
  }
  .brand-back .brand-dot { width: 11px; height: 11px; background: var(--gold); }
  .divider {
    position: absolute; left: 256px; top: 36px; width: 2px; height: 116px; background: var(--gold);
  }
  .contact {
    position: absolute; left: 276px; top: 38px;
    font-size: 16px; line-height: 1.3; font-weight: 300; color: var(--teal-soft);
  }
  .contact .name { color: var(--gold); font-size: 18px; font-weight: 400; margin-bottom: 10px; }
  .contact .phone { margin-bottom: 6px; }
  .dots {
    position: absolute; height: 0; border-top: 2px dotted var(--gold-dot);
  }
  .dots--contact { left: 276px; right: 30px; top: 170px; }
  .dots--appt { left: 222px; right: 30px; top: 222px; }
  .dots--appt2 { left: 30px; right: 30px; top: 270px; }
  .appt-label {
    position: absolute; left: 30px; top: 207px;
    font-size: 15px; letter-spacing: 1px; color: var(--teal-soft); text-transform: uppercase;
  }
</style>
</head>
<body>
<main class="stage">
  <section class="card card--front" aria-label="Card front">
    <div class="brand-front"><span class="brand-dot"></span>Petal Mist Care</div>
    <div class="front-rule"></div>
    <p class="tagline">calm roots bright petals</p>
  </section>

  <section class="card card--back" aria-label="Card back">
    <div class="brand-back"><span class="brand-dot"></span>Petal Mist Care</div>
    <div class="divider"></div>
    <div class="contact">
      <p class="name">Mira Trelawney</p>
      <p class="phone">907-318-2957</p>
      <p>2865 W Tamsen</p>
      <p>Sitkin Harbor, AK 99672</p>
    </div>
    <div class="dots dots--contact"></div>
    <p class="appt-label">Next Appointment</p>
    <div class="dots dots--appt"></div>
    <div class="dots dots--appt2"></div>
  </section>
</main>
</body>
</html>
```